Lueur de Provins Immerse in the enchanting flavors of France at Lueur de Provins

A menu that is French in style with the Eiffel Tower. A elegant menu that is in rich blue with red or gold trimmings, we are a French Bakey and Cafe

Target Market(s)

30 to 55 people

Industry/Entity Type

Restaurant

Font styles to use
Decorative

Colors
0054AA
0677BA
7BADD7
CADEEF
E8F1F8
EB3D1F
EC4F4E
F09395
F8D3D4
FCEDEE

Requirements
Must have
• the attachment "My Brunch Specials" is the Menu I want you to create, it has all the text, "My Brunch Special Complete" is a word version. The menu size should be 4 1/4 wide by 14 inches long 2 Sided. must have our logo at the top , Make the font larger, because our biggest complaint about our menu is it is hard to read
Nice to have
• I would love to incorporate the Eiffel Tower as a silhouette in the background
Should not have
• I do not want too many pictures or small print

```html
<!DOCTYPE html>
<html lang="en">
<head>
<meta charset="utf-8">
<title>Lueur de Provins — Menu</title>
<link href="https://fonts.googleapis.com/css2?family=Oswald:wght@300;400&family=Roboto:wght@400;500&display=swap" rel="stylesheet">
<style>
  :root {
    --navy: #1c2b52;
    --red: #c9393a;
    --ink: #1f2430;
    --mist: #ececec;
    --paper: #ffffff;
    --page: #ffffff;
  }
  * { box-sizing: border-box; margin: 0; padding: 0; }
  html, body { width: 1200px; height: 2721px; overflow: hidden; background: var(--page); }
  body { position: relative; font-family: "Roboto", Arial, sans-serif; color: var(--ink); }

  .brand-header { position: absolute; top: 120px; left: 0; width: 1200px; text-align: center; }
  .brand-name {
    font-family: "Roboto", Arial, sans-serif; font-weight: 500;
    font-size: 48px; letter-spacing: 0; color: var(--navy);
    display: inline-flex; align-items: center; gap: 18px;
  }
  .brand-mark { width: 22px; height: 22px; background: var(--navy); display: inline-block; }

  .menu-panel {
    position: absolute; top: 330px; width: 560px; height: 2360px;
    background: var(--paper); box-shadow: 0 6px 24px rgba(0,0,0,.08);
    display: flex; flex-direction: column; overflow: hidden;
  }
  .menu-panel--brunch { left: 25px; }
  .menu-panel--drinks { left: 615px; }

  .panel-crest {
    background: var(--mist); border-radius: 0 0 50% 50% / 0 0 34% 34%;
    height: 250px; display: flex; align-items: center; justify-content: center;
  }
  .panel-crest .brand-name { font-size: 30px; gap: 12px; }
  .panel-crest .brand-mark { width: 14px; height: 14px; }

  .panel-body {
    position: relative; flex: 1; padding: 20px 52px 24px;
    display: flex; flex-direction: column; justify-content: space-between;
  }
  .panel-body::before, .panel-body::after {
    content: ""; position: absolute; top: 0; bottom: 0; width: 12px;
  }
  .panel-body::before { left: 0; background: var(--navy); }
  .panel-body::after { right: 0; background: var(--red); }

  .section-title {
    display: flex; align-items: center; justify-content: center; gap: 14px;
    font-family: "Oswald", "Arial Narrow", sans-serif; font-weight: 300;
    font-size: 38px; letter-spacing: 0.06em; color: var(--navy); text-transform: uppercase;
  }
  .flourish { width: 60px; height: 14px; border-radius: 7px; background: var(--navy); opacity: .75; }

  .dish { text-align: center; }
  .dish-title {
    position: relative; display: flex; align-items: center; justify-content: center; margin-bottom: 12px;
  }
  .dish-title::before {
    content: ""; position: absolute; left: 70px; right: 70px; top: 50%; height: 7px; transform: translateY(-50%);
    background: linear-gradient(var(--navy) 0 2px, #fff 2px 5px, var(--red) 5px 7px);
  }
  .dish-title span {
    position: relative; background: var(--paper); border: 1.5px solid var(--red);
    padding: 3px 16px; font-weight: 500; font-size: 21px; color: var(--red);
  }
  .dish p { font-size: 14.5px; line-height: 1.5; }

  .tower-ornament {
    height: 110px; margin: 0 40px 10px; border-radius: 50% 50% 8px 8px / 30% 30% 8px 8px;
    background: linear-gradient(to top, var(--navy), rgba(28,43,82,.25));
  }
  .panel-footer {
    background: var(--mist); height: 230px; display: flex; align-items: center; justify-content: center;
  }
  .panel-footer .brand-name { font-size: 28px; gap: 12px; }
  .panel-footer .brand-mark { width: 13px; height: 13px; }
  .menu-panel--drinks .panel-body { padding-top: 30px; }
</style>
</head>
<body>
  <header class="brand-header">
    <div class="brand-name"><i class="brand-mark"></i>Lueur de Provins</div>
  </header>

  <section class="menu-panel menu-panel--brunch">
    <div class="panel-crest">
      <div class="brand-name"><i class="brand-mark"></i>Lueur de Provins</div>
    </div>
    <div class="panel-body">
      <h2 class="section-title"><span class="flourish" role="img" aria-label="Scroll ornament"></span>Brunch Specials<span class="flourish" role="img" aria-label="Scroll ornament"></span></h2>

      <article class="dish"><h3 class="dish-title"><span>Ratatouille &amp; eggs $18</span></h3>
        <p>Experience the essence of Provence with our Ratatouille, a vibrant medley of roasted squash, peppers, tomatoes, eggplant, infused with fragrant fresh herbs. Served with two perfectly poached eggs, and your choice of flavorful andouille sausage or crispy bacon. Accompanied by a side of crusty baguette. It's a hearty dish that celebrates the flavors of the Mediterranean countryside.</p></article>

      <article class="dish"><h3 class="dish-title"><span>Le Grande Breakfast $15</span></h3>
        <p>Start your day in style with our Le Grande Breakfast, a feast fit for royalty. Customize your morning indulgence with two eggs cooked to your preference, paired with either savory bacon or succulent chicken sausage. Choose between a freshly baked baguette or a buttery croissant to accompany your meal. Complete your breakfast by selecting from an array of sides including crispy hash browns, savory roasted potatoes, or a refreshing fruit salad. Bon appetit!</p></article>

      <article class="dish"><h3 class="dish-title"><span>Smoked Salmon Tartine $14</span></h3>
        <p>Delight in the luxurious flavors of our Smoked Salmon Tartine, a culinary masterpiece that elevates breakfast to new heights. Indulge in truffled scrambled eggs nestled atop smoked salmon, adorned with tangy pickled red onions, briny caper berries, crisp cucumber, juicy tomato, and peppery arugula. All artfully arranged on multigrain bread generously spread with herb-infused cream cheese.</p></article>

      <article class="dish"><h3 class="dish-title"><span>Le Benedict Salmon $14</span></h3>
        <p>Savor the classic elegance of Eggs Benedict, featuring two perfectly poached eggs nestled on toasted English muffins, with luscious smoked salmon and ripe tomato slices crowned with a velvety lemon-infused Hollandaise sauce. A timeless brunch delight crafted to perfection.</p></article>

      <article class="dish"><h3 class="dish-title"><span>Salmon Atlantique $14</span></h3>
        <p>Enjoy a bed of crisp mixed greens adorned with delicate smoked salmon, sweet golden raisins, creamy goat cheese, and crunchy walnuts. All dressed in a tantalizing balsamic vinaigrette that ties the elements together perfectly.</p></article>

      <article class="dish"><h3 class="dish-title"><span>Beef Bourguignon $18</span></h3>
        <p>Indulge in our rich and comforting flavors of savory, tender beef slowly braised in red wine, creating a luscious sauce that envelops pearl onions, carrots, and mushrooms in a symphony of flavors. Served alongside buttered egg noodles. It's a hearty and soul-warming meal that promises pure culinary bliss.</p></article>

      <article class="dish"><h3 class="dish-title"><span>Tourte au Poulet $15</span></h3>
        <p>Discover the indulgent flavors of our Tourte au Poulet, a savory delight that marries tender marinated chicken with the richness of Swiss cheese and the sweetness of onions, all encased in layers of flaky pastry. Topped with a savory mushroom medley and decadent bechamel sauce. A true comfort classic to delight your senses.</p></article>

      <div class="tower-ornament" role="img" aria-label="Eiffel Tower silhouette framed by scroll flourishes"></div>
    </div>
  </section>

  <section class="menu-panel menu-panel--drinks">
    <div class="panel-body">
      <h2 class="section-title"><span class="flourish" role="img" aria-label="Scroll ornament"></span>Drink Specials<span class="flourish" role="img" aria-label="Scroll ornament"></span></h2>

      <article class="dish"><h3 class="dish-title"><span>Bottomless Mimosa $18</span></h3>
        <p>Embark on an endless journey of delight with our Bottomless Mimosa, featuring Belcourt champagne, infusing each sip with a sparkling sensation. Tailor your experience with your preferred flavor profile - opt for the timeless twist of classic orange juice or tangy cranberry juice for a refreshing zing. Continuously poured to ensure your glass is always full.</p></article>

      <article class="dish"><h3 class="dish-title"><span>Apple Cider-Mimosa $9</span></h3>
        <p>A delightful twist on the classic mimosa. Crafted with champagne and crisp apple cider. To elevate the experience, we adorn the glass with a caramel rim dipped in brown sugar, adding a touch of indulgent sweetness to every sip.</p></article>

      <article class="dish"><h3 class="dish-title"><span>Blood Orange or Pineapple Spritz $12</span></h3>
        <p>Introducing our vibrant spritz cocktail, a tantalizing blend of Rouvin. Blend &amp; premium Vostrava Vodka, sweet vermouth, and a touch of sweetness from a carefully muddled sugar cube. This effervescent libation reaches new heights with the addition of bubbly Fontaine Claire, your choice of either Blood Orange or Pineapple syrup injects a burst of fruity allure into every sip.</p></article>

      <article class="dish"><h3 class="dish-title"><span>Peach Bellini $9</span></h3>
        <p>Try our perfectly balanced Peach Bellini with each sip you capture the crispness of champagne with the irresistible sweetness of peach. It's a sublime fusion of sophistication and sweetness.</p></article>

      <article class="dish"><h3 class="dish-title"><span>Espresso Martini $10</span></h3>
        <p>Our Espresso Martini is a decadent blend of bold espresso, rich chocolate martini, and luxurious Maison Belvaux chocolate syrup. It's the ultimate indulgence for coffee and chocolate lovers alike.</p></article>

      <article class="dish"><h3 class="dish-title"><span>Kir Royale $10</span></h3>
        <p>Our Kir Royale is a delightful fusion of the crisp, sparkling champagne bubbles and the sweet sophistication of black currant. a luxurious and indulgent drink that's perfect for any occasion.</p></article>

      <h2 class="section-title"><span class="flourish" role="img" aria-label="Scroll ornament"></span>Latte<span class="flourish" role="img" aria-label="Scroll ornament"></span></h2>

      <article class="dish"><h3 class="dish-title"><span>Truffle Latte $6</span></h3>
        <p>We start with rich Maison Belvaux chocolate, known for its velvety smoothness and intense flavor. Then, we add a drizzle of salted caramel, adding a perfect balance of sweetness and a hint of savory richness. Finally, we combine this delightful blend with perfectly steamed milk to create a creamy and indulgent latte that will satisfy even the most discerning palate.</p></article>

      <article class="dish"><h3 class="dish-title"><span>Napoleon Latte $6</span></h3>
        <p>We start with rich Maison Belvaux chocolate, known for its velvety smoothness and intense flavor. Then, we add a drizzle of salted caramel, adding a perfect balance of sweetness and a hint of savory richness. Finally, we combine this delightful blend with perfectly steamed milk to create a creamy and indulgent latte that will satisfy even the most discerning palate.</p></article>

      <article class="dish"><h3 class="dish-title"><span>Chai Latte $6</span></h3>
        <p>Our robust chai tea concentrate, infused with a symphony of cinnamon, cardamom, cloves, and ginger, sets the stage for a journey of aromatic delight. Paired with velvety steamed milk, each sip offers a harmonious blend of bold spices and creamy richness. Topped with a sprinkle of cinnamon, it's the perfect finishing touch to this comforting treat.</p></article>
    </div>
    <div class="panel-footer">
      <div class="brand-name"><i class="brand-mark"></i>Lueur de Provins</div>
    </div>
  </section>
</body>
</html>
```